Visitenkarten-Design für Garten- und Landschaftspflege
Tamuga Vent setzte meine Vorstellungen absolut super um ich kann Ihn nur weiter empfehlen. vielen dank
Zielgruppe
Baumpflege, Baumfällung, Garten und Landschaftspflege meine zielgruppe sind Privatpersonen im alter von 20-100Jahren
Aufgabenstellung
Sehr geehrte Damen und Herren, die visitenkarte sollte die angaben so enthalten wie sie auf der von mir gestallteten Visitenkarten sind ( meine ist kein maß der Dinge). Ich habe mein Logo leider nur als 3.jpg Datei. Das Logo darf im Design erändert werden aber bitte nur Feinheiten ansonsten stehen ihnen alle türen offen um kreativ zu sein.
mit freundlichen Grüßen Holger Banzow

```html
<!DOCTYPE html>
<html lang="de">
<head>
<meta charset="utf-8">
<title>Visitenkarten Baumpflege Banzow – Farbvarianten</title>
<link rel="stylesheet" href="https://fonts.googleapis.com/css2?family=Open+Sans:wght@400;700&family=Arimo:wght@400&display=swap">
<style>
  :root{
    --paper:#ffffff;
    --card:#dde6ad;
    --stripe:#cbdc80;
    --ground:#cfd8a0;
    --ink-black:#111111;
    --ink-dark:#333333;
    --ink-grey:#5e5e5e;
  }
  html,body{margin:0;padding:0;overflow:hidden}
  body{width:860px;height:1200px;background:var(--paper);position:relative;font-family:"Open Sans",Arial,sans-serif}
  .variant{position:absolute;left:149px;width:534px;height:165px}
  .variant--1{top:67px;--logo:var(--ink-black);--text:var(--ink-black)}
  .variant--2{top:273px;--logo:var(--ink-dark);--text:var(--ink-dark)}
  .variant--3{top:491px;--logo:var(--ink-grey);--text:var(--ink-grey)}
  .variant--4{top:713px;--logo:var(--ink-black);--text:var(--ink-grey)}
  .variant--5{top:930px;--logo:var(--ink-black);--text:var(--ink-grey)}
  .card{position:absolute;top:0;width:255px;height:165px;background:var(--card);box-shadow:3px 4px 6px rgba(0,0,0,.22);overflow:hidden}
  .card--front{left:0}
  .card--back{left:279px}
  .card::after{content:"";position:absolute;left:0;right:0;bottom:0;height:8px;background:var(--ground)}
  .stripe{position:absolute;top:0;bottom:0;width:13px;background:var(--stripe);z-index:1}
  .card--front .stripe{right:0}
  .card--back .stripe{left:0}
  .brand{position:absolute;margin:0;text-align:center;font-weight:700;color:var(--logo);text-transform:uppercase;line-height:1.05}
  .card--front .brand{left:0;right:13px;top:76px;font-size:15px;letter-spacing:.5px}
  .card--back .brand{left:143px;width:101px;top:52px;font-size:10px;letter-spacing:.3px}
  .brand__mark{display:block;width:10px;height:10px;margin:0 auto 6px;background:var(--logo)}
  .card--back .brand__mark{width:7px;height:7px;margin-bottom:4px}
  .services{position:absolute;left:19px;top:26px;margin:0;padding:0;list-style:none;font-size:7.2px;line-height:9.2px;color:var(--text)}
  .services li::before{content:"· "}
  .holder{position:absolute;left:19px;top:102px;color:var(--text)}
  .holder__name{margin:0;font-size:10.5px;letter-spacing:.4px;line-height:11px}
  .holder__title{margin:0;font-family:Arimo,Arial,sans-serif;font-size:4.3px;line-height:5.6px;text-align:right}
  .contact{position:absolute;left:143px;top:103px;font-family:Arimo,Arial,sans-serif;font-size:7.2px;line-height:9.2px;color:var(--text);font-style:normal}
  .contact p{margin:0}
  .contact__lines{margin-top:4px !important}
</style>
</head>
<body>

<section class="variant variant--1">
  <div class="card card--front"><span class="stripe"></span>
    <p class="brand"><span class="brand__mark"></span>Baumpflege<br>Banzow</p></div>
  <div class="card card--back"><span class="stripe"></span>
    <ul class="services"><li>Kronenpflege &amp; Einkürzung</li><li>Fällung</li><li>Obstbaumschnitt</li><li>Beratung vor Ort</li></ul>
    <p class="brand"><span class="brand__mark"></span>Baumpflege<br>Banzow</p>
    <div class="holder"><p class="holder__name">Holger Banzow</p><p class="holder__title">Fachagrarwirt für Baumpflege<br>&amp; Baumsanierung</p></div>
    <address class="contact"><p>Lindenweg 4</p><p>85600 Moosach</p><p class="contact__lines">0170 / 555 21 48</p><p>kontakt@baumpflege-banzow.de</p><p>baumpflege-banzow.de</p></address></div>
</section>

<section class="variant variant--2">
  <div class="card card--front"><span class="stripe"></span>
    <p class="brand"><span class="brand__mark"></span>Baumpflege<br>Banzow</p></div>
  <div class="card card--back"><span class="stripe"></span>
    <ul class="services"><li>Kronenpflege &amp; Einkürzung</li><li>Fällung</li><li>Obstbaumschnitt</li><li>Beratung vor Ort</li></ul>
    <p class="brand"><span class="brand__mark"></span>Baumpflege<br>Banzow</p>
    <div class="holder"><p class="holder__name">Holger Banzow</p><p class="holder__title">Fachagrarwirt für Baumpflege<br>&amp; Baumsanierung</p></div>
    <address class="contact"><p>Lindenweg 4</p><p>85600 Moosach</p><p class="contact__lines">0170 / 555 21 48</p><p>kontakt@baumpflege-banzow.de</p><p>baumpflege-banzow.de</p></address></div>
</section>

<section class="variant variant--3">
  <div class="card card--front"><span class="stripe"></span>
    <p class="brand"><span class="brand__mark"></span>Baumpflege<br>Banzow</p></div>
  <div class="card card--back"><span class="stripe"></span>
    <ul class="services"><li>Kronenpflege &amp; Einkürzung</li><li>Fällung</li><li>Obstbaumschnitt</li><li>Beratung vor Ort</li></ul>
    <p class="brand"><span class="brand__mark"></span>Baumpflege<br>Banzow</p>
    <div class="holder"><p class="holder__name">Holger Banzow</p><p class="holder__title">Fachagrarwirt für Baumpflege<br>&amp; Baumsanierung</p></div>
    <address class="contact"><p>Lindenweg 4</p><p>85600 Moosach</p><p class="contact__lines">0170 / 555 21 48</p><p>kontakt@baumpflege-banzow.de</p><p>baumpflege-banzow.de</p></address></div>
</section>

<section class="variant variant--4">
  <div class="card card--front"><span class="stripe"></span>
    <p class="brand"><span class="brand__mark"></span>Baumpflege<br>Banzow</p></div>
  <div class="card card--back"><span class="stripe"></span>
    <ul class="services"><li>Kronenpflege &amp; Einkürzung</li><li>Fällung</li><li>Obstbaumschnitt</li><li>Beratung vor Ort</li></ul>
    <p class="brand"><span class="brand__mark"></span>Baumpflege<br>Banzow</p>
    <div class="holder"><p class="holder__name">Holger Banzow</p><p class="holder__title">Fachagrarwirt für Baumpflege<br>&amp; Baumsanierung</p></div>
    <address class="contact"><p>Lindenweg 4</p><p>85600 Moosach</p><p class="contact__lines">0170 / 555 21 48</p><p>kontakt@baumpflege-banzow.de</p><p>baumpflege-banzow.de</p></address></div>
</section>

<section class="variant variant--5">
  <div class="card card--front"><span class="stripe"></span>
    <p class="brand"><span class="brand__mark"></span>Baumpflege<br>Banzow</p></div>
  <div class="card card--back"><span class="stripe"></span>
    <ul class="services"><li>Kronenpflege &amp; Einkürzung</li><li>Fällung</li><li>Obstbaumschnitt</li><li>Beratung vor Ort</li></ul>
    <p class="brand"><span class="brand__mark"></span>Baumpflege<br>Banzow</p>
    <div class="holder"><p class="holder__name">Holger Banzow</p><p class="holder__title">Fachagrarwirt für Baumpflege<br>&amp; Baumsanierung</p></div>
    <address class="contact"><p>Lindenweg 4</p><p>85600 Moosach</p><p class="contact__lines">0170 / 555 21 48</p><p>kontakt@baumpflege-banzow.de</p><p>baumpflege-banzow.de</p></address></div>
</section>

</body>
</html>
```